Dental Office Postcard Promotion

Looking for an attractive design for our next post card advertisement campaign. We would like to point out a few specific items.
Great Dental Team - see pic 1.
On-Site Dental Lab - see pic 2.
End of Year insurance benefits - can be anything to symbolize this.
On back of card, I'd like to show our call to action which is a Verano Brightpulse Tooth brush - image can be found online.
The postcard is 4'' x 6'' in size. Our website is maplecrestsmiles.example. The address to this office is 4172 W Ridgefield Road, Ashbrook Falls, NC and phone number is (555) 314-7092.

-

Target Market(s)

Community mailbox holders

Industry/Entity Type

Dental

Font styles to use
Serif

Colors
0054AA
0677BA
7BADD7
CADEEF
E8F1F8
0094D4
00A9DD
6FCCEA
C7EBF8
E9F6FB
00AB8E
00BBA5
67D7C9
C6EFE9
E9F9F6

Requirements
Must have
• Color scheme and logo from website listed.
Nice to have
• A nice layout of the provided pictures (and others requested). An attractive call to action page.
Should not have
• Advertising should be subtle, not like a flash sale for used cars.

```html
<!DOCTYPE html>
<html lang="en">
<head>
<meta charset="utf-8">
<title>Maplecrest Smiles Postcard – Two Type Options</title>
<link rel="stylesheet" href="https://fonts.googleapis.com/css2?family=Tinos:ital,wght@0,400;0,700;1,400;1,700&family=Montserrat:ital,wght@0,500;0,700;1,600;1,700&display=swap">
<style>
:root{
  --stage:#ececec;
  --card:#f8f9fa;
  --brand-blue:#2b6cb3;
  --brand-green:#4cae52;
  --band-start:#00addf;
  --band-end:#2c6db5;
  --ring:#2a6ab1;
  --photo-a:#d9d9d9;
  --photo-b:#8a8f96;
  --cal-red:#f04e4e;
  --white:#ffffff;
}
*{box-sizing:border-box;margin:0;padding:0}
html,body{width:1200px;height:460px;overflow:hidden;background:var(--stage)}
.stage{position:relative;width:1200px;height:460px}
.card{position:absolute;top:82px;width:439px;height:296px;background:var(--card);overflow:hidden}
.card--serif{left:108px;font-family:"Tinos","Times New Roman",serif}
.card--sans{left:652px;font-family:"Montserrat",Arial,sans-serif}
.card > *{position:absolute;white-space:nowrap}
.headline{left:15px;top:17px;font-size:14px;font-style:italic;color:var(--brand-blue)}
.phone{left:14px;top:39px;font-size:23px;font-style:italic;color:var(--brand-blue)}
.card--sans .headline{font-weight:700;font-size:13.5px;top:16px}
.card--sans .phone{font-weight:700;font-size:22px;top:38px}
.brand{left:18px;top:96px;color:var(--brand-blue);text-align:center;line-height:1}
.brand-name{display:block;font-size:17px;letter-spacing:1px}
.brand-sub{display:block;font-size:7px;letter-spacing:3px;margin-top:3px}
.website{left:15px;top:143px;font-size:12px;font-style:italic;color:var(--brand-green)}
.card--sans .website{font-weight:700;font-size:11px;top:141px}
.photo{width:110px;height:110px;border-radius:50%;border:2px solid var(--ring);background:radial-gradient(circle at 40% 60%,var(--photo-b),var(--photo-a) 70%)}
.photo--team{left:171px;top:63px}
.photo--lab{left:295px;top:14px}
.caption{font-size:15px;font-style:italic;color:var(--brand-blue)}
.caption--team{left:166px;top:175px}
.caption--lab{left:290px;top:125px}
.card--sans .caption{font-weight:700;font-size:13.5px}
.card--sans .caption--team{left:157px;top:174px}
.card--sans .caption--lab{left:282px;top:124px}
.bands{left:0;top:0;width:439px;height:296px}
.calendar{left:6px;top:209px;width:74px;height:74px;border-radius:50%;background:var(--white)}
.calendar svg{position:absolute;left:17px;top:14px}
.benefit{left:88px;top:236px;font-size:15px;line-height:19px;font-weight:700;color:var(--white)}
.card--sans .benefit{font-size:13px;line-height:17px;font-style:italic;top:237px}
.address{left:315px;top:242px;font-size:10px;line-height:14px;font-style:italic;color:var(--white)}
.card--sans .address{left:312px;top:259px;font-size:8.5px;line-height:12px;font-weight:700}
</style>
</head>
<body>
<main class="stage">

  <section class="card card--serif" aria-label="Postcard, serif option">
    <svg class="bands" viewBox="0 0 439 296" aria-hidden="true">
      <defs>
        <linearGradient id="bandSerif" x1="0" x2="1" y1="0" y2="0">
          <stop offset="0" stop-color="var(--band-start)"/>
          <stop offset="1" stop-color="var(--band-end)"/>
        </linearGradient>
      </defs>
      <path d="M0,210 C70,185 150,232 250,222 C330,214 390,196 439,228 L439,296 L0,296Z" fill="url(#bandSerif)"/>
      <path d="M12,198 C60,166 150,198 235,210 C320,222 385,170 439,207 L439,222 C390,192 325,214 250,222 C160,232 75,188 12,200Z" fill="var(--brand-green)"/>
    </svg>
    <p class="headline">Schedule Your Appointment Today !</p>
    <p class="phone">(555) 314-7092</p>
    <p class="brand"><span class="brand-name">MAPLECREST</span><span class="brand-sub">SMILES &amp; DENTURES</span></p>
    <p class="website">maplecrestsmiles.example</p>
    <div class="photo photo--team" role="img" aria-label="Photo of a dental team member checking a denture"></div>
    <div class="photo photo--lab" role="img" aria-label="Photo of a dentist talking with a patient in the on-site lab"></div>
    <p class="caption caption--team">Great Dental Team</p>
    <p class="caption caption--lab">On-Site Dental Lab</p>
    <div class="calendar">
      <svg width="40" height="46" viewBox="0 0 40 46" aria-hidden="true">
        <rect x="1" y="4" width="38" height="40" rx="3" fill="#fff" stroke="#e6e6e6"/>
        <rect x="1" y="4" width="38" height="11" rx="3" fill="var(--cal-red)"/>
        <text x="20" y="13" text-anchor="middle" font-family="Montserrat,sans-serif" font-size="8" font-weight="700" fill="#fff">DEC</text>
        <text x="20" y="36" text-anchor="middle" font-family="Montserrat,sans-serif" font-size="19" font-weight="700" fill="var(--cal-red)">31</text>
      </svg>
    </div>
    <p class="benefit">Your Dental Insurance Benefits<br>expire END OF YEAR.</p>
    <p class="address">4172 W Ridgefield Road,<br>Ashbrook Falls, NC</p>
  </section>

  <section class="card card--sans" aria-label="Postcard, sans option">
    <svg class="bands" viewBox="0 0 439 296" aria-hidden="true">
      <defs>
        <linearGradient id="bandSans" x1="0" x2="1" y1="0" y2="0">
          <stop offset="0" stop-color="var(--band-start)"/>
          <stop offset="1" stop-color="var(--band-end)"/>
        </linearGradient>
      </defs>
      <path d="M0,210 C70,185 150,232 250,222 C330,214 390,196 439,228 L439,296 L0,296Z" fill="url(#bandSans)"/>
      <path d="M12,198 C60,166 150,198 235,210 C320,222 385,170 439,207 L439,222 C390,192 325,214 250,222 C160,232 75,188 12,200Z" fill="var(--brand-green)"/>
    </svg>
    <p class="headline">Schedule Your Appointment Today !</p>
    <p class="phone">(555) 314-7092</p>
    <p class="brand"><span class="brand-name">MAPLECREST</span><span class="brand-sub">SMILES &amp; DENTURES</span></p>
    <p class="website">maplecrestsmiles.example</p>
    <div class="photo photo--team" role="img" aria-label="Photo of a dental team member checking a denture"></div>
    <div class="photo photo--lab" role="img" aria-label="Photo of a dentist talking with a patient in the on-site lab"></div>
    <p class="caption caption--team">Great Dental Team</p>
    <p class="caption caption--lab">On-Site Dental Lab</p>
    <div class="calendar">
      <svg width="40" height="46" viewBox="0 0 40 46" aria-hidden="true">
        <rect x="1" y="4" width="38" height="40" rx="3" fill="#fff" stroke="#e6e6e6"/>
        <rect x="1" y="4" width="38" height="11" rx="3" fill="var(--cal-red)"/>
        <text x="20" y="13" text-anchor="middle" font-family="Montserrat,sans-serif" font-size="8" font-weight="700" fill="#fff">DEC</text>
        <text x="20" y="36" text-anchor="middle" font-family="Montserrat,sans-serif" font-size="19" font-weight="700" fill="var(--cal-red)">31</text>
      </svg>
    </div>
    <p class="benefit">Your Dental Insurance Benefits<br>expire END OF YEAR.</p>
    <p class="address">4172 W Ridgefield Road,<br>Ashbrook Falls, NC</p>
  </section>

</main>
</body>
</html>
```